Lorcan Webpage Design

I would like to start an business and management consultancy business. I am thinking to called it "Movara Consultancy". Besides the consultancy services, I would also like to provide training on finance, forensic accounting, fraud prevention and internal control.
Professional management consultants are contracted by organizations to provide advisory services in an objective and independent manner.

Services include, but are not limited to, strategic planning, facilitation, quality assurance, education and training, investment counsel, identification and analysis of management problems, developing solutions, and the implementation of proposed solutions.

Professional management consultants are hired when an organization lacks sufficient resources, requires external objective advice, or because they have expertise not available within the client organization.

I would like to see the webpage design that use colors apple green with some other contrast color. The design have to be professional look but with a new age touch.

Reason: Unable to find a suitable web pages design

Dear all

Since last week I post a request, but till to date, I has yet to received a new sparkling creative and "wow" web page design. Please help me here!

Regards

Reason: Yet to found a suitable web designer for my web design. Help! I just need a fresh and professional look design. You may ignore the color code I prefer. Send me your sparkling creative work. Thank you so much!

Some examples

```html
<!DOCTYPE html>
<html lang="en">
<head>
<meta charset="utf-8">
<title>Movara Consultancy</title>
<link href="https://fonts.googleapis.com/css2?family=Ubuntu:wght@400;500;700&family=Roboto+Slab:wght@700&family=Roboto+Condensed:wght@700&display=swap" rel="stylesheet">
<style>
:root{
  --apple:#7fb800;
  --apple-dark:#5f8f00;
  --apple-light:#9ccf1c;
  --heading-green:#6aa51a;
  --blue:#1d8fe0;
  --blue-dark:#0f6fc0;
  --blue-light:#3fb2f5;
  --red:#c8171d;
  --ink:#222;
  --muted:#444;
  --paper:#f4f4f4;
  --sky:#d7e4ef;
}
*{margin:0;padding:0;box-sizing:border-box}
html,body{width:718px;height:1200px;overflow:hidden}
body{position:relative;font-family:"Ubuntu",Arial,sans-serif;color:var(--ink);
  background:linear-gradient(#fff 0,#fff 880px,var(--sky) 1135px)}
.abs{position:absolute}

/* header */
.site-header{left:0;top:0;width:718px;height:98px;background:linear-gradient(#fff,#ececec)}
.brand{left:66px;top:30px;display:flex;align-items:center;gap:10px}
.brand-dot{width:26px;height:26px;border-radius:50%;background:var(--apple)}
.brand-name{font:500 27px "Ubuntu",sans-serif;color:var(--apple)}
.call-btn{left:505px;top:38px;width:146px;height:30px;background:var(--red);border:1px solid #8e0f12;
  color:#fff;font:700 13px "Roboto Condensed",sans-serif;display:flex;align-items:center;justify-content:center}

/* nav */
.main-nav{left:0;top:98px;width:718px;height:38px;background:linear-gradient(var(--blue-light),var(--blue) 60%,var(--blue-dark));
  display:flex;align-items:center}
.main-nav a{position:absolute;color:#fff;font:700 10.5px "Ubuntu",sans-serif;text-decoration:none;text-transform:uppercase}

/* hero */
.hero{left:0;top:136px;width:718px;height:247px;background:radial-gradient(ellipse at 55% 10%,var(--apple-light),var(--apple) 55%,var(--apple-dark))}
.hero-photo{left:57px;top:22px;width:341px;height:199px;border:3px solid #fff;outline:3px solid var(--apple-dark);
  background:linear-gradient(120deg,#f3f3f3,#dcdcdc 50%,#fafafa)}
.hero-title{left:412px;top:43px;font:700 23px "Roboto Slab",serif;color:#fff;text-shadow:0 2px 2px rgba(0,0,0,.3)}
.hero-text{left:414px;top:76px;width:240px;font:700 14.5px/18px "Roboto Slab",serif;color:#fff}
.know-btn{left:415px;top:150px;width:113px;height:32px;background:linear-gradient(var(--blue-light),var(--blue-dark));
  border:1px solid #fff;color:#fff;font:700 13px "Roboto Condensed",sans-serif;display:flex;align-items:center;justify-content:center;gap:6px}
.hero-shadow{left:40px;top:383px;width:660px;height:14px;background:radial-gradient(ellipse at top,rgba(0,0,0,.18),transparent 70%)}

/* sections */
.section-title{font:700 13.5px "Ubuntu",sans-serif;color:var(--heading-green);text-transform:uppercase}
.about-img{left:54px;top:445px;width:381px;height:99px;border:1px solid #ccc;padding:3px;background:#fff}
.about-img div{width:100%;height:100%;background:linear-gradient(100deg,#cfe0ef,#9aa3ad 50%,#d8e6c0)}
.body-copy{font:400 8.4px/11.2px "Ubuntu",sans-serif;color:var(--muted);width:382px}

.review{left:54px;width:381px;height:58px}
.avatar{position:absolute;left:0;top:0;width:40px;height:35px;border:1px solid #ccc;background:linear-gradient(#e6cfa8,#b58b64)}
.review p{position:absolute;left:45px;top:0;width:336px;font:400 8.4px/11px "Ubuntu",sans-serif;color:#333;
  border-bottom:1px dashed #bbb;padding-bottom:4px}
.review a{position:absolute;right:0;top:44px;font:400 8.4px "Ubuntu",sans-serif;color:var(--blue-dark);text-decoration:none}

/* sidebar */
.hire-box{left:448px;top:418px;width:206px;height:58px;background:var(--apple);border:2px solid #c9e59a;padding:6px 8px;color:#fff;
  font:400 9px/13px Arial,sans-serif}
.hire-box b{display:block;font:700 10.5px "Ubuntu",sans-serif}
.hire-box .call{color:#111;font:700 9.5px "Ubuntu",sans-serif}
.card{background:#fff;box-shadow:0 2px 8px rgba(0,0,0,.25)}
.appt{left:450px;top:497px;width:204px;height:270px}
.appt h3{position:absolute;top:10px;width:100%;text-align:center}
.advisor{left:11px;top:34px;width:184px;height:227px;background:var(--blue);color:#fff;text-align:center}
.advisor .lead{margin-top:12px;font:italic 700 10.5px "Ubuntu",sans-serif}
.phone{display:flex;align-items:center;justify-content:center;gap:6px;margin-top:10px;font:700 14px "Ubuntu",sans-serif}
.or{font:700 17px "Ubuntu",sans-serif;margin-top:6px}
.note{font:400 7.8px/10px "Ubuntu",sans-serif;padding:0 16px;margin-top:4px}
.field{position:absolute;left:10px;width:168px;display:flex;align-items:center;justify-content:flex-end;gap:5px;font:400 8px "Ubuntu",sans-serif}
.field span{display:block;width:107px;height:17px;background:#fff;border:1px solid #999}
.submit{position:absolute;left:57px;top:191px;width:62px;height:23px;background:linear-gradient(var(--apple-light),var(--apple-dark));
  border:1px solid #e8f3d0;color:#111;font:700 11px "Ubuntu",sans-serif;display:flex;align-items:center;justify-content:center}
.touch{left:450px;top:789px;width:204px;height:82px}
.touch h3{position:absolute;top:9px;width:100%;text-align:center}
.social{position:absolute;top:38px;width:29px;height:29px;border-radius:50%}

/* services */
.service{top:951px;width:144px;height:150px;background:var(--paper);box-shadow:0 2px 6px rgba(0,0,0,.25)}
.service h4{height:29px;border-bottom:1px solid #ddd;text-align:center;line-height:29px;font:700 10.5px/29px Arial,sans-serif;color:var(--blue);text-transform:uppercase}
.service .pic{margin:9px 8px 0;height:57px;border:1px solid #ccc}
.service p{padding:6px 9px 0;font:400 8px/10px "Ubuntu",sans-serif;color:#222}
.service a{display:block;padding:6px 9px 0;font:400 7.5px "Ubuntu",sans-serif;color:var(--blue-dark);text-decoration:none}

/* footer */
.site-footer{left:0;top:1140px;width:718px;height:60px;background:var(--apple);border-top:3px solid #fff;
  box-shadow:0 -2px 0 var(--apple-dark);font:400 7.5px "Ubuntu",sans-serif;color:#222}
.site-footer .copy{position:absolute;left:54px;top:24px}
.site-footer .links{position:absolute;right:78px;top:24px;display:flex;gap:18px}
</style>
</head>
<body>

<header class="site-header abs">
  <div class="brand abs"><span class="brand-dot"></span><span class="brand-name">Movara Consultancy</span></div>
  <div class="call-btn abs">Call For An Appointment</div>
</header>

<nav class="main-nav abs">
  <a href="#" style="left:74px">Home</a>
  <a href="#" style="left:135px">About Us</a>
  <a href="#" style="left:212px">Services</a>
  <a href="#" style="left:287px">Training</a>
  <a href="#" style="left:363px">Accounting</a>
  <a href="#" style="left:457px">Fraud Prevention</a>
  <a href="#" style="left:580px">Contact Us</a>
</nav>

<section class="hero abs">
  <div class="hero-photo abs" role="img" aria-label="Photo of a smiling consultant in a suit presenting a bar chart"></div>
  <h1 class="hero-title abs">FINANCIAL PROBLEM!</h1>
  <p class="hero-text abs">Movara Consultancy provide you help on each section of your financail problem.</p>
  <div class="know-btn abs">KNOW MORE
    <svg width="16" height="16" viewBox="0 0 16 16"><circle cx="8" cy="8" r="6.5" fill="none" stroke="#fff" stroke-width="1.6"/><path d="M5 8h5M8 5.5 10.5 8 8 10.5" fill="none" stroke="#fff" stroke-width="1.6"/></svg>
  </div>
</section>
<div class="hero-shadow abs"></div>

<h2 class="section-title abs" style="left:54px;top:419px">About Us</h2>
<div class="about-img abs"><div role="img" aria-label="Illustration of a calculator beside colourful bar chart figures"></div></div>
<p class="body-copy abs" style="left:54px;top:557px">Lorem ipsum dolor sit amet, consectetur adipiscing elit. Ut sagittis, nulla non malesuada lacinia, eros sapien rhoncus odio, eget semper ante leo tempor ipsum. Integer mi urna, hendrerit vitae ornare a, egestas eget mauris. Sed a erat at purus mattis sollicitudin a a ante. Nam posuere tempus posuere. Pellentesque hendrerit, metus vel ornare facilisis, justo neque interdum enim, ut volutpat massa sem congue arcu. Quisque quis odio magna.</p>
<p class="body-copy abs" style="left:54px;top:624px">Cum sociis natoque penatibus et magnis dis parturient montes, nascetur ridiculus mus. Nunc tincidunt massa non dolor dictum aliquam. Vivamus sit amet sapien. Sed a erat at purus mattis sollicitudin a a ante. Nam posuere tempus posuere. Pellentesque hendrerit, metus vel ornare facilisis, justo neque interdum enim, ut volutpat massa sem congue arcu. Quisque quis odio magna.</p>

<h2 class="section-title abs" style="left:54px;top:689px">What Our Client Says?</h2>
<div class="review abs" style="top:716px"><div class="avatar" role="img" aria-label="Client portrait"></div><p>Does what it says on the tin – and does it well!<br>Simple concept, simply delivered. Effective, efficient. Just like this review would have been if it didn't have to be at...</p><a href="#">Read Full Review</a></div>
<div class="review abs" style="top:783px"><div class="avatar" role="img" aria-label="Client portrait"></div><p>Does what it says on the tin – and does it well!<br>Simple concept, simply delivered. Effective, efficient...</p><a href="#">Read Full Review</a></div>
<div class="review abs" style="top:851px"><div class="avatar" role="img" aria-label="Client portrait"></div><p>Does what it says on the tin – and does it well!<br>Simple concept, simply delivered. Effective, efficient. Just like this review would have been if it didn't have to be at...</p><a href="#">Read Full Review</a></div>

<aside>
  <div class="hire-box abs">Are You A<b>Professional Management Consultant?</b><span class="call">CALL US, WE WILL HIRE YOU</span></div>

  <div class="appt card abs">
    <h3 class="section-title">Ask For An Appontment</h3>
    <div class="advisor abs">
      <p class="lead">SPEAK TO A FINANCIAL ADVISOR</p>
      <div class="phone">
        <svg width="22" height="22" viewBox="0 0 22 22"><rect x="1" y="3" width="20" height="16" rx="3" fill="#8cc63f"/><path d="M7 7c1 3 4 6 7 7l1.5-1.5 2 1.5-1 2c-5 0-10-5-10-10l2-1 1.5 2z" fill="#fff"/></svg>
        91.8600.4372
      </div>
      <p class="or">OR</p>
      <p class="note">Fill the form below one of our financial advisor will contact you shortly</p>
      <div class="field" style="top:108px">Name:<span></span></div>
      <div class="field" style="top:132px">Email id<span></span></div>
      <div class="field" style="top:156px">Contact No:<span></span></div>
      <div class="submit">SUBMIT</div>
    </div>
  </div>

  <div class="touch card abs">
    <h3 class="section-title">Get In Touch With Us</h3>
    <span class="social" style="left:36px;background:#2f4f9a"></span>
    <span class="social" style="left:71px;background:#20a4e4"></span>
    <span class="social" style="left:107px;background:#c9322a"></span>
    <span class="social" style="left:143px;background:#f29a1f"></span>
  </div>
</aside>

<h2 class="section-title abs" style="left:57px;top:925px">Special Services</h2>
<article class="service abs" style="left:54px"><h4>Strategic Planning</h4><div class="pic" role="img" aria-label="Photo of a team discussing around a laptop" style="background:linear-gradient(#b89a84,#6d6a7a)"></div><p>Lorem ipsum dolor sit amer est di maria ..</p><a href="#">Read More····›</a></article>
<article class="service abs" style="left:208px"><h4>Quality Assurance</h4><div class="pic" role="img" aria-label="Photo of a businessman working at a desk" style="background:linear-gradient(#d8d2c8,#4b4b4b)"></div><p>Lorem ipsum dolor sit amer est di maria ..</p><a href="#">Read More····›</a></article>
<article class="service abs" style="left:362px"><h4>Education &amp; Training</h4><div class="pic" role="img" aria-label="Photo of a presenter in front of a large chart display" style="background:linear-gradient(90deg,#5a6f86,#b7d3ea)"></div><p>Lorem ipsum dolor sit amer est di maria ..</p><a href="#">Read More····›</a></article>
<article class="service abs" style="left:516px"><h4>Developing Solutions</h4><div class="pic" role="img" aria-label="Illustration of a rising bar chart on a screen" style="background:linear-gradient(#fafafa,#bdbdbd)"></div><p>Lorem ipsum dolor sit amer est di maria ..</p><a href="#">Read More····›</a></article>

<footer class="site-footer abs">
  <span class="copy">© Movara Consultancy, All Rights Reserved 2013,</span>
  <span class="links"><span>Terms &amp; conditions</span><span>|</span><span>Faq</span><span>|</span><span>About</span><span>|</span><span>Contact</span></span>
</footer>

</body>
</html>
```